eBook Cover

Here is the book title: 27 LESSONS EACH MINISTER SHOULD
LEARN ABOUT FINANCES

Here is the subtitle (or author section): A Harvest Lantern eBook

I've attached the harvest lantern logo below.

Target Market(s)

Church Pastors

Requirements
Must have
• Lantern Logo and Harvest Lantern color palette.
Nice to have
• I have attached some sample book covers that I like

```html
<!DOCTYPE html>
<html lang="en">
<head>
<meta charset="utf-8">
<title>27 Lessons Each Minister Should Learn About Finances — A Harvest Lantern eBook</title>
<link rel="stylesheet" href="https://fonts.googleapis.com/css2?family=League+Gothic&family=Oswald:wght@700&display=swap">
<style>
  :root {
    --cover-yellow: #ffc62b;
    --cover-yellow-light: #ffd54a;
    --title-white: #ffffff;
    --ink: #121212;
    --band-black: #0c0c0c;
    --note-green-light: #d9dccb;
    --note-green-dark: #9ea48c;
  }
  html, body {
    margin: 0;
    padding: 0;
    width: 800px;
    height: 1200px;
    overflow: hidden;
    background: var(--cover-yellow);
  }
  .cover {
    position: relative;
    width: 800px;
    height: 1200px;
    overflow: hidden;
    background: radial-gradient(ellipse at 50% 45%, var(--cover-yellow-light) 0%, var(--cover-yellow) 70%);
    font-family: "League Gothic", "Oswald", sans-serif;
  }

  .publisher {
    position: absolute;
    top: 52px;
    left: 0;
    width: 100%;
    display: flex;
    align-items: center;
    justify-content: center;
    gap: 14px;
  }
  .publisher-mark {
    width: 22px;
    height: 22px;
    border-radius: 50%;
    background: var(--ink);
  }
  .publisher-name {
    color: var(--ink);
    font-family: "Oswald", sans-serif;
    font-weight: 700;
    font-size: 32px;
    line-height: 1;
    letter-spacing: 2px;
    text-transform: uppercase;
  }

  .title {
    margin: 0;
    color: var(--title-white);
    font-weight: 400;
    text-transform: uppercase;
  }
  .title-line {
    position: absolute;
    left: 0;
    width: 100%;
    text-align: center;
    white-space: nowrap;
    line-height: 1;
  }
  .title-line--first  { top: 170px; font-size: 103px; letter-spacing: 2px; }
  .title-line--second { top: 237px; font-size: 273px; letter-spacing: 1px; }
  .title-line--third  { top: 483px; font-size: 94px;  letter-spacing: 3px; }
  .title-line--fourth { top: 543px; font-size: 273px; letter-spacing: 1px; }

  .banknote {
    position: absolute;
    top: 868px;
    left: 262px;
    width: 330px;
    height: 136px;
    transform: rotate(-6deg);
    background: linear-gradient(135deg, var(--note-green-light), var(--note-green-dark));
    box-shadow: 0 6px 10px rgba(0, 0, 0, 0.25);
  }

  .imprint-band {
    position: absolute;
    left: 0;
    bottom: 0;
    width: 100%;
    height: 112px;
    background: var(--band-black);
    display: flex;
    align-items: center;
    justify-content: center;
  }
  .imprint {
    margin: 0;
    color: var(--cover-yellow);
    font-size: 80px;
    font-weight: 400;
    letter-spacing: 2px;
    text-transform: uppercase;
    line-height: 1;
  }
</style>
</head>
<body>
  <main class="cover">
    <div class="publisher">
      <span class="publisher-mark"></span>
      <span class="publisher-name">The Lantern Company</span>
    </div>

    <h1 class="title">
      <span class="title-line title-line--first">27 Lessons Each</span>
      <span class="title-line title-line--second">Minister</span>
      <span class="title-line title-line--third">Should Learn About</span>
      <span class="title-line title-line--fourth">Finances</span>
    </h1>

    <div class="banknote" role="img" aria-label="Photograph of a one-dollar bill lying at a slight angle"></div>

    <footer class="imprint-band">
      <p class="imprint">A Harvest Lantern eBook</p>
    </footer>
  </main>
</body>
</html>
```